Cedar Hollow Candle Banner Ad for Upcoming holidays

We would like for you to design an ad for Memorial day and Father's Day. For Memorial Day the sale will be 25% OFF select candles and free shipping when you order $50 or more.
For father's day the deal will be get 30% off all candles and free shipping when you order $75 or more.
Please note: These banners will be on our website, they do not require our logo.Banner size: 314 height x 783 width

Industry/Entity Type

Shipping

Requirements
Must have
• Banner size: 314 height x 783 width
Nice to have
• Picture of our starlit candle
Should not have
• Logo

```html
<!DOCTYPE html>
<html lang="en">
<head>
<meta charset="utf-8">
<title>Cedar Hollow Candle – Memorial Day Sale</title>
<link rel="stylesheet" href="https://fonts.googleapis.com/css2?family=Cinzel:wght@400&family=Baloo+2:wght@800&family=Space+Mono:wght@700&display=swap">
<style>
  :root {
    --paper: #ffffff;
    --sky-light: #c9a3a0;
    --sky-mid: #9a6664;
    --sky-deep: #5e2c2e;
    --band: rgba(38, 24, 24, 0.78);
    --headline: #e58c5f;
    --badge: #0b0b0b;
    --badge-text: #ffffff;
    --ink: #111111;
    --jar-cream: #e9e3da;
    --jar-teal: #69b7c3;
  }
  html, body {
    margin: 0;
    padding: 0;
    width: 1200px;
    height: 481px;
    overflow: hidden;
    background: var(--paper);
  }
  .banner {
    position: relative;
    width: 1200px;
    height: 481px;
    background: var(--paper);
  }
  .banner svg { display: block; }
  .headline {
    font-family: "Cinzel", "Times New Roman", serif;
    font-weight: 400;
    fill: var(--headline);
  }
  .offer {
    font-family: "Baloo 2", "Arial Rounded MT Bold", sans-serif;
    font-weight: 800;
    fill: var(--badge-text);
  }
  .shipping {
    font-family: "Space Mono", "Courier New", monospace;
    font-weight: 700;
    fill: var(--ink);
  }
</style>
</head>
<body>
<main class="banner">
  <svg width="1200" height="481" viewBox="0 0 1200 481" xmlns="http://www.w3.org/2000/svg">
    <defs>
      <linearGradient id="sky" x1="0" y1="0" x2="0" y2="1">
        <stop offset="0" stop-color="var(--sky-deep)"/>
        <stop offset="0.35" stop-color="var(--sky-light)"/>
        <stop offset="0.6" stop-color="var(--sky-mid)"/>
        <stop offset="1" stop-color="var(--sky-deep)"/>
      </linearGradient>
      <linearGradient id="jars" x1="0" y1="0" x2="1" y2="0">
        <stop offset="0" stop-color="var(--jar-cream)"/>
        <stop offset="0.55" stop-color="var(--jar-cream)"/>
        <stop offset="0.56" stop-color="var(--jar-teal)"/>
        <stop offset="1" stop-color="var(--jar-teal)"/>
      </linearGradient>
    </defs>

    <g class="sky-panels" role="img" aria-label="Dusky rose cloudy sky split into four panels">
      <rect x="15" y="15" width="529" height="253" fill="url(#sky)"/>
      <rect x="555" y="15" width="637" height="253" fill="url(#sky)"/>
      <rect x="15" y="280" width="529" height="157" fill="url(#sky)"/>
      <rect x="555" y="280" width="637" height="157" fill="url(#sky)"/>
    </g>

    <rect class="headline-band" x="15" y="64" width="1177" height="98" fill="var(--band)"/>
    <text class="headline" x="61" y="138" font-size="74" textLength="1073" lengthAdjust="spacing">MEMORIAL DAY</text>

    <rect class="product" x="230" y="222" width="314" height="244" rx="18"
          fill="url(#jars)" role="img"
          aria-label="Two Cedar Hollow Candle starlit three-wick candle jars, cream and teal, with a silver lid"/>

    <circle class="badge" cx="1066" cy="300" r="134" fill="var(--badge)"/>
    <text class="offer" x="1066" y="302" font-size="100" text-anchor="middle">25%</text>
    <text class="offer" x="1066" y="382" font-size="88" text-anchor="middle" letter-spacing="6">OFF</text>

    <text class="shipping" x="590" y="472" font-size="28" textLength="590" lengthAdjust="spacing">&amp;free shipping for +$50</text>
  </svg>
</main>
</body>
</html>
```